Wealth Education Business Needs Sharp Business Card Design

We need a business card design for a recently launched investor education business called Harbor Crest.

The final design should promote security, empowerment, self improvement and financial gain. The card will ideally promote the stature of the business.

For more information and colours please visit harborcrest.com.au

Target Market(s)

Corporate executives and high net worth individuals

Industry/Entity Type

Education

Contact Information for Business Card

Name
Position
Contact Address
Phone
Mobile
Email
Website

```html
<!DOCTYPE html>
<html lang="en">
<head>
<meta charset="utf-8">
<title>Harbor Crest – Business Card</title>
<link rel="stylesheet" href="https://fonts.googleapis.com/css2?family=Lato:wght@400;700&display=swap">
<style>
  :root {
    --backdrop: #2b2b2d;
    --deep-teal: #0f3b3a;
    --deep-teal-light: #1d4f4d;
    --brand-teal: #0f6a66;
    --name-teal: #2b8a86;
    --band-top: #7ea3a5;
    --band-bottom: #2f666a;
    --swoosh-blue: #2f9bd6;
    --ink: #3a3a3a;
    --paper: #ffffff;
  }
  * { margin: 0; padding: 0; box-sizing: border-box; }
  html, body {
    width: 1200px; height: 800px; overflow: hidden;
    background: var(--backdrop);
    font-family: "Lato", Arial, sans-serif;
  }
  .canvas { position: relative; width: 1200px; height: 800px; }

  .card {
    position: absolute;
    top: 254px;
    width: 510px; height: 292px;
    border-radius: 4px;
    overflow: hidden;
    box-shadow: 0 10px 30px rgba(0,0,0,0.45);
  }

  /* Front side */
  .card-front {
    left: 60px;
    background: linear-gradient(135deg, var(--deep-teal-light), var(--deep-teal));
    display: flex; align-items: center; justify-content: center;
  }
  .wordmark {
    display: flex; align-items: center; gap: 14px;
    font-weight: 400; letter-spacing: 0.22em; text-transform: uppercase;
  }
  .card-front .wordmark { color: var(--paper); font-size: 30px; }
  .wordmark-dot { width: 16px; height: 16px; border-radius: 50%; background: currentColor; }

  /* Back side */
  .card-back { left: 630px; background: var(--paper); }
  .card-back .artwork { position: absolute; inset: 0; }
  .card-back .wordmark {
    position: absolute; top: 26px; left: 0; right: 0; justify-content: center;
    color: var(--ink); font-size: 22px;
  }
  .card-back .wordmark-dot { background: var(--brand-teal); width: 13px; height: 13px; }

  .holder {
    position: absolute; top: 62px; left: 0; right: 0; text-align: center;
  }
  .holder-name { color: var(--name-teal); font-size: 27px; line-height: 1.1; }
  .holder-role { color: var(--ink); font-size: 11px; line-height: 1.2; }

  .contact-list { position: absolute; list-style: none; color: var(--paper); font-size: 13px; }
  .contact-list li { display: flex; align-items: center; gap: 8px; height: 20px; }
  .contact-list svg { width: 13px; height: 13px; fill: var(--paper); flex: none; }
  .contact-online { left: 330px; top: 124px; }
  .contact-office { left: 44px; top: 204px; }

  .address {
    position: absolute; right: 16px; top: 236px; width: 140px;
    color: var(--paper); font-size: 12.5px; line-height: 1.3; text-align: right;
  }
</style>
</head>
<body>
<main class="canvas">

  <section class="card card-front" aria-label="Card front">
    <div class="wordmark"><span>Harbor</span><span class="wordmark-dot"></span><span>Crest</span></div>
  </section>

  <section class="card card-back" aria-label="Card back">
    <svg class="artwork" viewBox="0 0 510 292" aria-hidden="true">
      <defs>
        <linearGradient id="bandFill" x1="0" y1="0" x2="0" y2="1">
          <stop offset="0" stop-color="var(--band-top)"/>
          <stop offset="1" stop-color="var(--band-bottom)"/>
        </linearGradient>
      </defs>
      <rect class="contact-band" x="22" y="114" width="470" height="138" rx="22" fill="url(#bandFill)" opacity="0.92"/>
      <path class="swoosh" d="M282 292 C308 222 392 172 510 154 L510 165 C400 186 322 230 300 292 Z" fill="var(--swoosh-blue)"/>
      <path class="corner-panel" d="M316 292 C336 236 400 196 510 180 L510 292 Z" fill="var(--brand-teal)"/>
    </svg>

    <div class="wordmark"><span>Harbor</span><span class="wordmark-dot"></span><span>Crest</span></div>

    <div class="holder">
      <p class="holder-name">Owen Hartley</p>
      <p class="holder-role">Director</p>
    </div>

    <ul class="contact-list contact-online">
      <li><svg viewBox="0 0 16 16"><path d="M4 0h8a1 1 0 0 1 1 1v14a1 1 0 0 1-1 1H4a1 1 0 0 1-1-1V1a1 1 0 0 1 1-1zm0 2v11h8V2zm4 11.5a.8.8 0 1 0 0 1.6.8.8 0 0 0 0-1.6z"/></svg>111 444 4567</li>
      <li><svg viewBox="0 0 16 16"><path d="M8 0a8 8 0 1 0 0 16A8 8 0 0 0 8 0zm5.9 7h-2.6a12 12 0 0 0-1-5 6 6 0 0 1 3.6 5zM8 2c.7.9 1.2 2.7 1.3 5H6.7C6.8 4.7 7.3 2.9 8 2zM5.7 2a12 12 0 0 0-1 5H2.1a6 6 0 0 1 3.6-5zM2.1 9h2.6a12 12 0 0 0 1 5 6 6 0 0 1-3.6-5zM8 14c-.7-.9-1.2-2.7-1.3-5h2.6c-.1 2.3-.6 4.1-1.3 5zm2.3 0a12 12 0 0 0 1-5h2.6a6 6 0 0 1-3.6 5z"/></svg>www.yourweb.com</li>
    </ul>

    <ul class="contact-list contact-office">
      <li><svg viewBox="0 0 16 16"><path d="M1 4c0-2 3-3 7-3s7 1 7 3v1.5h-3.5V4h-7v1.5H1zM4 7h8l2 7H2zm4 1.5a2 2 0 1 0 0 4 2 2 0 0 0 0-4z"/></svg>000 111 2122</li>
      <li><svg viewBox="0 0 16 16"><path d="M0 3h16v10H0zm1.5 1.2v.3L8 9l6.5-4.5v-.3zm0 2.1V11.5h13V6.3L8 10.8z"/></svg>name@yourweb.com</li>
    </ul>

    <p class="address">Your home or business address here</p>
  </section>

</main>
</body>
</html>
```